Website Redesign for Existing BBQ Catering Company

Need to get my website (HickoryHound.com) redesigned. Looking for a cleaner look but still patriotic and rustic. Would like to add parallax scrolling on the menu page and include some pics from our photo gallery. Would like to display a picture of the brisket before scrolling into the meat section of our menu and the same for the other sections too.....picture of one of our sides, appetizers, desserts, etc.

Would also like to add three new pages called Corporate Events, Weddings, and Veteran Events possibly in a drop-down menu called Catering. You can use pics from our Facebook page. We've posted tons of pics from weddings that we've done. I've uploaded some corporate and wedding pics but you can pics the ones that look best. I can swap them out later if needed.

Would like to keep it Wordpress if possible so I can update it as needed.

Also need to add some links to our storefront on The Vow Loft. I have the HTML code and will upload the image here.

Also need to add social media links for our Facebook, Instagram and Twitter pages.

The contact form that I'm using now feeds the leads into another site called Ledgerly.com that I use to manage my clients.

Target Market(s)

Weddings, corporate events, veterans

Industry/Entity Type

Catering

Coding

Coded - Design and coding required

Number of Pages Required

5+ page

Colors
ec1f27
3176b5
ffffff

Requirements
Must have
• Really like the hero image design. Looks less like a template. Check out https://maurins.com and https://fennelgrovetaos.com
• Would like to keep somewhat of a rustic and patriotic look and feel like the site currently is. We mainly cater in barn weddings and we cater for a lot of veterans. Will be pushing more corporate catering next year and opening a restaurant.

```html
<!DOCTYPE html>
<html lang="en">
<head>
<meta charset="utf-8">
<title>Hickory Hound BBQ – Catering</title>
<link href="https://fonts.googleapis.com/css2?family=Rye&family=Roboto+Slab:wght@400;700&display=swap" rel="stylesheet">
<style>
:root{
  --red:#ec1f27;
  --blue:#3176b5;
  --white:#ffffff;
  --ink:#1e1e1e;
  --charcoal:#2e2e2e;
  --charcoal-dark:#262626;
  --paper:#efeeec;
  --wood-light:#8a5a36;
  --wood-dark:#4a2c18;
  --muted:#cfcfcf;
}
*{box-sizing:border-box;margin:0;padding:0}
html,body{width:1200px;height:4663px;overflow:hidden}
body{position:relative;font-family:"Roboto Slab",Georgia,serif;color:var(--ink);background:var(--paper)}
.abs{position:absolute}
.display{font-family:"Rye",Georgia,serif;font-weight:400}

/* header + hero */
.hero{left:0;top:0;width:1200px;height:637px;background:linear-gradient(180deg,#3a2418 0%,#7a4a2a 40%,#5a3320 75%,#2a1a10 100%)}
.site-header{left:0;top:0;width:1200px;height:118px;background:linear-gradient(180deg,rgba(255,255,255,.97),rgba(255,255,255,.9))}
.brand{left:120px;top:20px;display:flex;align-items:center;gap:10px}
.brand-dot{width:34px;height:34px;border-radius:50%;background:var(--red)}
.brand-name{font-size:20px;font-weight:700;color:var(--blue)}
.topinfo{top:28px;font-size:13px;color:#444;display:flex;align-items:center;gap:7px}
.social{display:flex;gap:7px}
.social span{width:14px;height:14px;border-radius:50%;background:var(--blue);display:block}
.nav{left:535px;top:74px;display:flex;gap:38px;font-size:15px;font-weight:700;letter-spacing:.5px}
.nav a{color:var(--ink);text-decoration:none}
.nav a.active{color:var(--red)}
.btn{display:inline-block;background:var(--red);color:var(--white);font-weight:700;text-align:center;text-decoration:none;letter-spacing:.5px}
.contact-btn{left:935px;top:66px;width:128px;height:34px;line-height:34px;font-size:13px}
.badge-best{left:513px;top:249px;width:187px;height:72px;background:var(--blue);border:4px solid var(--red);color:var(--white);font-size:30px;line-height:64px;text-align:center}
.badge-meat{left:440px;top:340px;width:320px;height:82px;background:rgba(30,20,15,.45);border:3px solid var(--white);color:var(--white);font-size:34px;line-height:76px;text-align:center}
.hero-btn{left:513px;top:436px;width:156px;height:48px;line-height:48px;font-size:17px}

/* torn edges */
.edge{left:0;width:1200px}

/* about */
.about{left:0;top:637px;width:1200px;height:500px;background:radial-gradient(ellipse at 60% 50%,#3b3b3b,var(--charcoal-dark))}
.grill-art{left:124px;top:690px;width:342px;height:360px;border-radius:50% 50% 12px 12px;background:radial-gradient(circle at 50% 40%,#9b4a2c,#5d2a18 60%,#3a3a3a 61%,#2f2f2f)}
.about-kicker{left:530px;top:737px;color:var(--white);font-size:18px;font-weight:700;letter-spacing:1px}
.about-title{left:530px;top:762px;color:var(--white);font-size:28px}
.about-text{left:530px;top:812px;width:560px;color:#dcdcdc;font-size:13.5px;line-height:1.62}
.about-btn{left:530px;top:996px;width:120px;height:34px;line-height:34px;font-size:12px}

/* events */
.events{left:0;top:1137px;width:1200px;height:640px;background:linear-gradient(90deg,var(--wood-dark),var(--wood-light) 30%,#6b4126 55%,var(--wood-light) 80%,var(--wood-dark))}
.event-card{top:1244px;width:452px;height:374px;border:6px solid var(--white);box-shadow:0 6px 16px rgba(0,0,0,.45)}
.event-photo{position:absolute;inset:0}
.event-title{position:absolute;left:0;right:0;top:118px;text-align:center;color:var(--white);font-size:38px;line-height:1.05;text-shadow:0 2px 4px rgba(0,0,0,.6)}
.event-btn{position:absolute;left:76px;top:266px;width:288px;height:56px;line-height:56px;font-size:20px}

/* gallery */
.gallery{left:0;top:1772px;width:1200px;height:770px;background:var(--paper)}
.section-title{width:1200px;left:0;text-align:center;font-size:46px;letter-spacing:2px}
.gallery-grid{left:134px;top:1949px;width:932px;display:grid;grid-template-columns:238px 232px 232px 230px;grid-template-rows:246px 240px;row-gap:43px}
.gallery-grid div{height:100%}

/* menu */
.menu{left:0;top:2534px;width:1200px;height:1712px;background:linear-gradient(90deg,#3e2414,#7d4e2d 25%,#5c3620 50%,#7d4e2d 75%,#3e2414)}
.menu-title{top:2640px;color:var(--white)}
.dish-photo{}
.menu-card{background:var(--white);padding:40px 46px 30px 46px;box-shadow:0 8px 22px rgba(0,0,0,.45)}
.menu-card h3{font-family:"Rye",Georgia,serif;font-weight:400;font-size:30px;letter-spacing:1px;margin-bottom:22px}
.menu-item{margin-bottom:16px}
.menu-item h4{font-size:15px;font-weight:700;margin-bottom:3px}
.menu-item p{font-size:11.5px;line-height:1.45;color:#444}
.scroll-bar{position:absolute;right:20px;top:100px;width:4px;height:210px;background:#ddd}
.scroll-bar::after{content:"";position:absolute;left:-1px;top:10px;width:6px;height:40px;background:var(--ink)}

/* footer */
.footer{left:0;top:4244px;width:1200px;height:419px;background:var(--charcoal)}
.foot-col h5{font-family:"Rye",Georgia,serif;font-weight:400;color:var(--white);font-size:22px;letter-spacing:1px;margin-bottom:22px}
.foot-col p{color:#cfcfcf;font-size:12px;line-height:1.6}
.foot-col.center{text-align:center}
.field{width:310px;height:40px;background:#3c3c3c;border:1px solid #4a4a4a;margin-bottom:10px;color:#aaa;font-size:12px;padding:10px 12px}
.field.tall{height:80px}
.submit{width:120px;height:38px;line-height:38px;font-size:13px;margin:18px auto 0;display:block}
</style>
</head>
<body>

<!-- HERO -->
<div class="abs hero" role="img" aria-label="Close-up of a smoked rack of ribs garnished with herbs"></div>
<header class="abs site-header">
  <div class="abs brand"><span class="brand-dot"></span><span class="brand-name">Hickory Hound BBQ</span></div>
  <div class="abs topinfo" style="left:684px">
    <svg width="12" height="12" viewBox="0 0 12 12"><circle cx="6" cy="6" r="5" fill="none" stroke="#555" stroke-width="1.4"/><path d="M6 3v3l2 1.5" stroke="#555" stroke-width="1.3" fill="none"/></svg>
    On Site Foods 24/7
  </div>
  <div class="abs topinfo" style="left:822px">
    <svg width="12" height="12" viewBox="0 0 12 12"><path d="M2 1.5l2.5-.5 1.2 2.8-1.5 1a6 6 0 0 0 3 3l1-1.5 2.8 1.2-.5 2.5C5.5 10.5 1.5 6.5 2 1.5z" fill="#555"/></svg>
    555-014-2287
  </div>
  <div class="abs topinfo social" style="left:966px"><span></span><span></span><span></span><span></span></div>
  <nav class="abs nav">
    <a class="active" href="#">HOME</a><a href="#">ABOUT</a><a href="#">OUR MENU</a><a href="#">GALLERY</a>
  </nav>
  <a class="abs btn contact-btn" href="#">CONTACT US</a>
</header>
<div class="abs badge-best display">BEST BBQ</div>
<div class="abs badge-meat display">PREMIUM MEAT</div>
<a class="abs btn hero-btn" href="#">RESERVE NOW</a>

<!-- ABOUT -->
<section class="abs about"></section>
<svg class="abs edge" style="top:622px" height="30" viewBox="0 0 1200 30" preserveAspectRatio="none"><polygon fill="#303030" points="0,30 0,14 40,10 90,18 150,8 210,16 270,6 330,15 400,9 460,17 520,7 590,14 650,10 720,18 790,8 850,15 920,9 990,17 1050,8 1120,15 1200,10 1200,30"/></svg>
<div class="abs grill-art" role="img" aria-label="Illustration of a kettle grill loaded with ribs and sausages"></div>
<div class="abs about-kicker">ABOUT US</div>
<h2 class="abs about-title display">SMOKED SLOW &amp; LOW BBQ</h2>
<p class="abs about-text">Hickory Hound is a new BBQ catering company opened with a mission to give back to the veteran community. As the name suggests, Hickory Hound is a patriotic initiative started by a veteran and his wife who are passionate about BBQ and engaging in business with an objective and purpose. At Hickory Hound, we cherish our heroes and would like to remind all citizens that it's the heroes who make our nation great. Our mission coincides with the pledge to care for those who have borne the battle, for their families and for their survivors, by serving and honoring the men and women who are America's veterans.</p>
<a class="abs btn about-btn" href="#">READ MORE</a>

<!-- EVENTS -->
<section class="abs events" role="img" aria-label="Rustic dark wooden plank background"></section>
<article class="abs event-card" style="left:134px">
  <div class="event-photo" role="img" aria-label="Barn wedding reception hall with string lights" style="background:linear-gradient(160deg,#6b3a1c,#a7652c 45%,#3a2010)"></div>
  <h3 class="event-title display">WEDDING<br>PARTY</h3>
  <a class="btn event-btn" href="#">RESERVE NOW</a>
</article>
<article class="abs event-card" style="left:612px">
  <div class="event-photo" role="img" aria-label="Guests at an outdoor veteran event" style="background:linear-gradient(160deg,#5d6a5a,#8d8a78 45%,#3c3a34)"></div>
  <h3 class="event-title display">VETERAN<br>PARTY</h3>
  <a class="btn event-btn" href="#">RESERVE NOW</a>
</article>

<!-- GALLERY -->
<section class="abs gallery"></section>
<svg class="abs edge" style="top:1752px" height="36" viewBox="0 0 1200 36" preserveAspectRatio="none"><polygon fill="#efeeec" points="0,36 0,16 50,22 110,10 170,20 230,12 300,24 360,14 430,20 490,8 560,18 620,12 690,24 760,10 820,20 890,14 950,22 1020,10 1080,18 1140,12 1200,20 1200,36"/></svg>
<h2 class="abs section-title display" style="top:1830px">OUR GALLERY</h2>
<div class="abs gallery-grid">
  <div role="img" aria-label="Rustic BBQ sign on a wooden table" style="background:linear-gradient(135deg,#d8d2c8,#8e8272)"></div>
  <div role="img" aria-label="Catering buffet with chafing dishes" style="background:linear-gradient(135deg,#6a5440,#c4a276)"></div>
  <div role="img" aria-label="Buffet line in a barn venue" style="background:linear-gradient(135deg,#3c3026,#a38a62)"></div>
  <div role="img" aria-label="Wooden decor at a wedding venue" style="background:linear-gradient(135deg,#efe9df,#8d6c48)"></div>
  <div role="img" aria-label="BBQ smoker trailer outdoors" style="background:linear-gradient(135deg,#5d5448,#24201c)"></div>
  <div role="img" aria-label="Catering team standing together" style="background:linear-gradient(135deg,#9b8a72,#3a3430)"></div>
  <div role="img" aria-label="Serving trays of smoked meat" style="background:linear-gradient(135deg,#a38366,#4c3a2a)"></div>
  <div role="img" aria-label="Event tables with BBQ signage" style="background:linear-gradient(135deg,#c9c1b4,#2c2a28)"></div>
</div>

<!-- MENU -->
<section class="abs menu" role="img" aria-label="Warm wooden plank background"></section>
<svg class="abs edge" style="top:2520px" height="40" viewBox="0 0 1200 40" preserveAspectRatio="none"><polygon fill="#efeeec" points="0,0 1200,0 1200,18 1140,26 1080,14 1010,28 950,16 880,24 820,12 760,26 690,16 620,28 560,14 490,24 430,12 360,26 300,16 230,24 170,12 110,26 50,14 0,22"/></svg>
<h2 class="abs section-title menu-title display">OUR MENU</h2>

<div class="abs" style="left:134px;top:2751px;width:460px;height:426px;background:radial-gradient(circle at 45% 50%,#f4efe6,#c8b8a0 60%,#7a5638)" role="img" aria-label="Breakfast plate with bacon, egg, tomatoes and beans"></div>
<div class="abs menu-card" style="left:590px;top:2792px;width:476px;height:363px">
  <h3>APPETIZER</h3>
  <div class="menu-item"><h4>Combo Sliders</h4><p>Brisket &amp; pulled pork sliders served with all three of our BBQ sauces on the side.</p></div>
  <div class="menu-item"><h4>Mini Brisket Tacos</h4><p>Smoked brisket wrapped in a mini corn tortilla topped with pico, cheese and guac on the side.</p></div>
  <div class="menu-item"><h4>Mini Brisket Tacos</h4><p>Smoked brisket wrapped in a mini corn tortilla topped with pico, cheese and guac on the side.</p></div>
  <span class="scroll-bar"></span>
</div>

<div class="abs" style="left:535px;top:3233px;width:531px;height:429px;background:radial-gradient(circle at 50% 55%,#a5442a,#6a2616 55%,#d7cfc2 56%,#efebe4)" role="img" aria-label="Glazed rack of smoked ribs on a cutting board"></div>
<div class="abs menu-card" style="left:134px;top:3275px;width:420px;height:363px">
  <h3>MAIN COURSE</h3>
  <div class="menu-item"><h4>Combo Sliders</h4><p>Brisket &amp; pulled pork sliders served with all three of our BBQ sauces on the side.</p></div>
  <div class="menu-item"><h4>Mini Brisket Tacos</h4><p>Smoked brisket wrapped in a mini corn tortilla topped with pico, cheese and guac on the side.</p></div>
  <div class="menu-item"><h4>Mini Brisket Tacos</h4><p>Smoked brisket wrapped in a mini corn tortilla topped with pico, cheese and guac on the side.</p></div>
  <span class="scroll-bar"></span>
</div>

<div class="abs" style="left:134px;top:3715px;width:531px;height:426px;background:radial-gradient(circle at 50% 50%,#d49a52,#b06e30 50%,#f2f0ec 51%,#7fa36a)" role="img" aria-label="Almond-topped dessert bake in a white dish"></div>
<div class="abs menu-card" style="left:640px;top:3760px;width:426px;height:363px">
  <h3>DESSERTS</h3>
  <div class="menu-item"><h4>Combo Sliders</h4><p>Brisket &amp; pulled pork sliders served with all three of our BBQ sauces on the side.</p></div>
  <div class="menu-item"><h4>Mini Brisket Tacos</h4><p>Smoked brisket wrapped in a mini corn tortilla topped with pico, cheese and guac on the side.</p></div>
  <div class="menu-item"><h4>Mini Brisket Tacos</h4><p>Smoked brisket wrapped in a mini corn tortilla topped with pico, cheese and guac on the side.</p></div>
  <span class="scroll-bar"></span>
</div>

<!-- FOOTER -->
<footer class="abs footer">
  <div class="abs foot-col center" style="left:150px;top:50px;width:260px">
    <h5>OUR LOCATION</h5>
    <p>48 Cedar Barn Road, Suite 2<br>Millbrook, FL 32700<br>United States</p>
    <p style="margin-top:16px">[phone] 555-014-2287<br>[e-mail] hello@hickoryhound.com</p>
    <div class="social" style="justify-content:center;margin-top:16px"><span></span><span></span><span></span><span></span></div>
  </div>
  <div class="abs foot-col center" style="left:440px;top:50px;width:270px">
    <h5>WORKING HOURS</h5>
    <p>Monday To Friday<br>8:00am to 10:00pm (Breakfast)<br>11:00am to 10:00pm (Lunch/Dinner)</p>
    <p style="margin-top:16px">Saturday &amp; Sunday<br>10:00am to 11:00pm (Brunch)<br>11:00am to 10:00pm (Lunch/Dinner)</p>
  </div>
  <div class="abs foot-col" style="left:762px;top:50px;width:310px">
    <h5 style="text-align:center">FEEDBACK FORM</h5>
    <div class="field">Name</div>
    <div class="field">Email</div>
    <div class="field">Phone</div>
    <div class="field tall">Message</div>
    <a class="btn submit" href="#">SUBMIT</a>
  </div>
</footer>
<svg class="abs edge" style="top:4228px" height="34" viewBox="0 0 1200 34" preserveAspectRatio="none"><polygon fill="#2e2e2e" points="0,34 0,14 60,20 120,8 190,18 250,10 320,22 380,12 450,18 510,6 580,16 640,10 710,22 770,10 840,18 900,12 970,20 1030,8 1100,18 1160,12 1200,16 1200,34"/></svg>

</body>
</html>
```